New Business Card Design Project

I need a meaningful new business card. Therefore, the website should convey growth, joy, uniqueness, workout and a bit of luxury.
Color scheme should be petrol, gold and matching colors.

```html
<!DOCTYPE html>
<html lang="de">
<head>
<meta charset="utf-8">
<title>Seeblick Studio – Visitenkarte</title>
<link rel="stylesheet" href="https://fonts.googleapis.com/css2?family=EB+Garamond:wght@400;500&family=Great+Vibes&display=swap">
<style>
  :root {
    --petrol: #17aaa0;
    --petrol-dark: #12958c;
    --gold: #c9a448;
    --graphite: #545659;
    --ink: #4a4a4a;
    --logo-ink: #34383a;
    --paper: #ffffff;
    --stage: #e9ebea;
  }
  * { box-sizing: border-box; margin: 0; padding: 0; }
  html, body { width: 1200px; height: 1122px; overflow: hidden; }
  body {
    background: var(--stage);
    position: relative;
    font-family: "EB Garamond", Georgia, serif;
  }
  .card {
    position: absolute;
    left: 170px;
    width: 860px;
    height: 490px;
    border-radius: 34px;
    border: 4px solid var(--gold);
    overflow: hidden;
  }
  .card--front { top: 40px; background: var(--petrol); }
  .card--back { top: 592px; background: var(--paper); }

  .brand {
    position: absolute;
    display: flex;
    align-items: center;
    gap: 14px;
    font-family: "EB Garamond", Georgia, serif;
    font-weight: 500;
    letter-spacing: 0.04em;
    white-space: nowrap;
  }
  .brand__dot {
    border-radius: 50%;
    flex: none;
  }
  .card--front .brand {
    left: 50%; top: 50%;
    transform: translate(-50%, -50%);
    font-size: 54px;
    color: var(--logo-ink);
  }
  .card--front .brand__dot { width: 22px; height: 22px; background: var(--logo-ink); }
  .card--back .brand {
    left: 46px; top: 200px;
    font-size: 38px;
    color: var(--petrol);
  }
  .card--back .brand__dot { width: 16px; height: 16px; background: var(--petrol); }

  .waves { position: absolute; left: 0; top: 0; width: 860px; height: 490px; }

  .holder {
    position: absolute;
    left: 370px;
    top: 44px;
  }
  .holder__name {
    font-family: "Great Vibes", cursive;
    font-size: 70px;
    line-height: 1;
    color: var(--petrol);
  }
  .holder__role {
    font-size: 27px;
    color: var(--ink);
    margin-top: 2px;
    margin-left: 24px;
  }
  .holder__rule {
    position: absolute;
    left: 392px;
    top: 166px;
    width: 470px;
    height: 2px;
    background: var(--petrol);
  }
  .contacts {
    position: absolute;
    left: 400px;
    top: 182px;
    list-style: none;
  }
  .contacts li {
    display: flex;
    align-items: center;
    gap: 14px;
    font-size: 23px;
    color: var(--ink);
    height: 34px;
    white-space: nowrap;
  }
  .contacts svg { width: 18px; height: 18px; flex: none; }
</style>
</head>
<body>

<section class="card card--front" aria-label="Vorderseite">
  <div class="brand"><span class="brand__dot"></span>Seeblick Studio</div>
</section>

<section class="card card--back" aria-label="Rückseite">
  <svg class="waves" viewBox="0 0 860 490" aria-hidden="true">
    <path d="M0 400 C 300 420, 600 400, 860 262 L860 490 L0 490 Z" fill="var(--graphite)"/>
    <path d="M0 422 C 300 442, 600 420, 860 276 L860 490 L0 490 Z" fill="var(--paper)"/>
    <path d="M0 430 C 300 450, 600 428, 860 282 L860 490 L0 490 Z" fill="var(--petrol)"/>
  </svg>

  <div class="brand"><span class="brand__dot"></span>Seeblick Studio</div>

  <div class="holder">
    <div class="holder__name">Lena Morgen</div>
    <div class="holder__role">Pilates Studio Trainerin</div>
  </div>
  <div class="holder__rule"></div>

  <ul class="contacts">
    <li>
      <svg viewBox="0 0 24 24"><path fill="var(--petrol)" d="M6.6 10.8a15.2 15.2 0 0 0 6.6 6.6l2.2-2.2a1 1 0 0 1 1-.25 11.4 11.4 0 0 0 3.6.57 1 1 0 0 1 1 1V20a1 1 0 0 1-1 1A17 17 0 0 1 3 4a1 1 0 0 1 1-1h3.5a1 1 0 0 1 1 1c0 1.25.2 2.45.57 3.57a1 1 0 0 1-.25 1z"/></svg>
      +49 151 2046 810
    </li>
    <li>
      <svg viewBox="0 0 24 24"><rect x="2" y="5" width="20" height="14" rx="1" fill="var(--petrol)"/><path d="M2 6l10 7 10-7" fill="none" stroke="#fff" stroke-width="1.6"/></svg>
      info@studio-seeblick.de
    </li>
    <li>
      <svg viewBox="0 0 24 24"><circle cx="12" cy="12" r="10" fill="var(--petrol)"/><path d="M2 12h20M12 2c3 3 3 17 0 20M12 2c-3 3-3 17 0 20" fill="none" stroke="#fff" stroke-width="1.4"/></svg>
      Studio-seeblick.de
    </li>
    <li>
      <svg viewBox="0 0 24 24"><circle cx="12" cy="12" r="8" fill="none" stroke="var(--petrol)" stroke-width="2.4"/></svg>
      balance_studiopractice
    </li>
  </ul>
</section>

</body>
</html>
```